New website design

Hello again, we need you to create a basic, standard website with a homepage, 'contact us' page with reply form, 'pricing page' and 'about us' page. We would like to see most design elements carried over from www.pilvarotek.com, our primary website. You can also use the front page of the attached brochure as inspiration for the homepage. The second attachment shows the pricing page (image on the right) with vertical columns - that's a good template for you to use on the pricing page for the website. The third attachment contains the text for the pricing page...just don't use that layout, try and duplicate the vertical layout example.
Target Market(s)
hospitals/medical care facilities
Coding
Coded - Design and coding required
Number of Pages Required
4 page

```html
<!DOCTYPE html>
<html lang="en">
<head>
<meta charset="utf-8">
<title>Pilvarotek Medical</title>
<link href="https://fonts.googleapis.com/css2?family=Poppins:wght@300;400;500;600;700;800&family=Montserrat:wght@400;500;600&display=swap" rel="stylesheet">
<style>
:root{
  --blue:#1a78b4;
  --blue-dark:#0e3f63;
  --navy:#1f2b3e;
  --ink:#1d2a3a;
  --text:#3c4654;
  --pale:#eef5fa;
  --line:#8fc0df;
  --white:#ffffff;
  --foot-text:#d6dde6;
}
*{margin:0;padding:0;box-sizing:border-box}
html,body{width:1200px;height:4016px;overflow:hidden;background:var(--white)}
body{position:relative;font-family:"Montserrat",sans-serif;color:var(--text)}
.abs{position:absolute}
h2.section-title{font-family:"Poppins",sans-serif;font-weight:400;font-size:38px;color:var(--ink);line-height:1.1;white-space:nowrap}
h2.section-title strong{font-weight:600;color:var(--blue)}
.rule{width:58px;height:3px;background:var(--blue);margin-top:14px}
.btn{position:absolute;display:flex;align-items:center;justify-content:center;border-radius:30px;font-family:"Poppins",sans-serif;font-weight:600;font-size:15px;letter-spacing:1.6px;text-transform:uppercase;text-decoration:none}
.btn.in-flow{position:relative;display:inline-flex}
.btn-solid{background:var(--blue);color:var(--white)}
.btn-outline{border:2px solid var(--blue);color:var(--blue);background:var(--white)}
p.body{font-size:15px;line-height:24px;color:var(--text)}

/* header */
.site-header{top:0;left:0;width:1200px;height:83px;background:var(--white);z-index:5}
.brand{left:101px;top:20px;display:flex;align-items:center;gap:10px}
.brand-dot{width:38px;height:38px;border-radius:50%;background:var(--blue)}
.brand-name{font-family:"Poppins",sans-serif;font-size:30px;font-weight:400;color:var(--blue)}
.main-nav a{position:absolute;top:30px;font-size:15px;color:var(--ink);text-decoration:none;font-weight:500;letter-spacing:.3px}
.main-nav a.active{color:var(--blue);font-weight:600}
.main-nav a.active::after{content:"";position:absolute;left:0;right:0;top:30px;height:3px;background:var(--blue)}

/* hero */
.hero{top:83px;left:0;width:1200px;height:700px;background:linear-gradient(90deg,#f1f5fa 0%,#e4ecf4 40%,#c7d6e6 100%)}
.hero-photo{top:83px;left:430px;width:770px;height:640px;background:linear-gradient(100deg,#e7eef6 0%,#a9c6e6 35%,#c9d3dd 65%,#8b9aab 100%)}
.hero-title{top:292px;left:97px;font-family:"Poppins",sans-serif;font-weight:800;font-size:40px;line-height:46px;color:var(--blue-dark);letter-spacing:.3px}
.hero-title span{color:var(--blue)}
.hero-sub{top:388px;left:97px;font-family:"Poppins",sans-serif;font-size:23px;color:var(--ink)}

/* about */
.about-photo{top:803px;left:106px;width:440px;height:370px;border-radius:50%;background:radial-gradient(circle at 45% 50%,#dfe6f0 0%,#6b7fa6 45%,#2d3b6e 70%,#f3f6fa 71%)}
.about-ring{top:800px;left:100px}
.about-copy{top:826px;left:589px;width:540px}

/* services */
.services{top:1275px;left:0;width:1200px;height:720px;background:linear-gradient(180deg,#0d5a80 0%,#1580b8 100%)}
.services-head{top:1325px;left:0;width:1200px;display:flex;flex-direction:column;align-items:center}
.services-head h2.section-title{color:var(--white);font-size:40px}
.services-head h2.section-title strong{color:var(--white)}
.services-head .rule{background:var(--white)}
.service-card{position:absolute;top:1418px;height:387px;border:2px solid rgba(160,210,240,.7);text-align:center;color:var(--white)}
.service-card .media{height:222px;margin:-2px -2px 0 -2px}
.service-card h3{font-family:"Poppins",sans-serif;font-weight:600;font-size:21px;margin-top:28px}
.service-card p{font-size:12px;line-height:20px;margin:10px auto 0;width:260px}
.service-card.featured{background:var(--white);border-color:var(--white);color:var(--ink);box-shadow:0 10px 30px rgba(0,0,0,.25)}
.service-card.featured p{color:var(--text)}

/* why */
.why-copy{top:2052px;left:109px;width:430px}
.why-frame{top:2010px;left:570px;width:200px;height:150px;border-top:3px solid var(--blue);border-left:3px solid var(--blue)}
.why-photo{top:2020px;left:584px;width:513px;height:372px;border-radius:0 100px 0 100px;background:linear-gradient(135deg,#3b4350 0%,#c7ccd3 40%,#e8ecf1 70%,#8fc3e6 100%)}

/* features */
.features{top:2489px;left:0;width:1200px;height:516px;background:var(--pale)}
.feature{position:absolute;top:2604px;width:314px;height:292px;border:2px solid var(--blue);text-align:center;padding-top:62px}
.feature h3{font-family:"Poppins",sans-serif;font-weight:400;font-size:27px;color:var(--ink)}
.feature h3 strong{font-weight:600;color:var(--blue)}
.feature p{font-size:12.5px;line-height:20px;width:260px;margin:20px auto 0}
.feature-icon{position:absolute;top:-47px;left:50%;margin-left:-55px;width:110px;height:94px;background:var(--pale);display:flex;justify-content:center;align-items:center}
.feature-icon .disc{width:90px;height:90px;border-radius:50%;background:var(--blue);display:flex;align-items:center;justify-content:center}
.feature-icon .disc.dark{background:var(--blue-dark)}

/* contact */
.contact-photo{top:3088px;left:122px;width:416px;height:406px;border-radius:50%;background:radial-gradient(circle at 60% 40%,#cdd8e3 0%,#9fb4c8 40%,#5e7f9d 75%,#2c3e52 100%)}
.contact-copy{top:3096px;left:600px}
.field{position:absolute;left:606px;width:447px;border:1.5px solid #9cc8e4;font-size:13px;color:#6b7685;padding:14px 18px;letter-spacing:.3px}

/* footer */
.site-footer{top:3622px;left:0;width:1200px;height:394px;background:var(--navy)}
.foot-brand{top:3755px;left:118px;display:flex;align-items:center;gap:12px}
.foot-brand .brand-dot{width:44px;height:44px}
.foot-brand .brand-name{color:#3c9ad6;font-size:26px}
.foot-sep{position:absolute;top:3622px;width:1px;height:274px;background:#3a4a60}
.foot-col{position:absolute;top:3696px;color:var(--foot-text)}
.foot-col h4{font-family:"Poppins",sans-serif;font-weight:600;font-size:17px;color:var(--white);border-left:3px solid var(--blue);padding-left:10px;margin-left:-14px}
.foot-col ul{list-style:none;margin-top:14px}
.foot-col li{font-size:12.5px;line-height:28px}
.foot-col .addr{font-size:12.5px;line-height:20px;margin-top:14px}
.social{display:flex;align-items:center;gap:14px;margin-top:22px}
.social .mark{width:22px;height:22px;border-radius:50%;border:2px solid var(--white)}
.social small{display:block;font-size:12.5px}
.social b{font-size:14px;color:var(--white);font-weight:600}
.foot-line{top:3951px;left:0;width:1200px;height:1px;background:#3a4a60}
.copyright{top:3970px;left:0;width:1200px;text-align:center;font-size:12px;color:#8a97a8}
</style>
</head>
<body>

<header class="abs site-header">
  <div class="abs brand"><span class="brand-dot"></span><span class="brand-name">Pilvarotek Medical</span></div>
  <nav class="main-nav">
    <a class="active" style="left:491px">HOME</a>
    <a style="left:592px">ABOUT US</a>
    <a style="left:725px">SERVICES</a>
    <a style="left:857px">PRICING</a>
    <a style="left:975px">CONTACT US</a>
  </nav>
</header>

<section>
  <div class="abs hero"></div>
  <div class="abs hero-photo" role="img" aria-label="Technician in cleanroom gown working at stainless steel processing equipment"></div>
  <h1 class="abs hero-title">CERTIFIED DIAGNOSTIC<br><span>AND REPAIR SERVICE</span></h1>
  <div class="abs hero-sub">FOR YOUR BIOMEDICAL EQUIPMENT</div>
  <a class="btn btn-solid" style="top:443px;left:95px;width:181px;height:50px">View Pricing</a>
  <svg class="abs" style="top:640px;left:0" width="1200" height="150" viewBox="0 0 1200 150">
    <path d="M0 140 C300 10 800 -10 1200 118 L1200 150 L0 150 Z" fill="#ffffff"/>
    <path d="M0 140 C300 10 800 -10 1200 118" fill="none" stroke="#1a78b4" stroke-width="10"/>
  </svg>
</section>

<section>
  <svg class="abs about-ring" width="450" height="380" viewBox="0 0 450 380">
    <path d="M190 8 A185 185 0 1 0 300 370" fill="none" stroke="#1a78b4" stroke-width="4"/>
  </svg>
  <div class="abs about-photo" role="img" aria-label="Sterilization chamber with open stainless steel door"></div>
  <div class="abs about-copy">
    <h2 class="section-title">About <strong>Pilvarotek Medical</strong></h2>
    <div class="rule"></div>
    <p class="body" style="margin-top:22px">Pilvarotek Medical Inc. offers efficient and FDA compliant assembly, packaging and in-house Hydrogen Peroxide Gas Plasma (HPGP) specific, as well as contract irradiation (gamma and e-beam) sterilization services for the medical device industry.</p>
    <p class="body" style="margin-top:16px">Validation services for manufacturing processes, packaging, and sterilization are customized to product specific</p>
    <a class="btn btn-outline in-flow" style="margin-top:26px;width:184px;height:54px">Learn More</a>
  </div>
</section>

<section>
  <div class="abs services"></div>
  <div class="abs services-head">
    <h2 class="section-title">Our <strong>Services</strong></h2>
    <div class="rule"></div>
  </div>
  <article class="service-card" style="left:126px;width:303px">
    <div class="media" role="img" aria-label="Gloved hand loading a tray into an autoclave" style="border-radius:0 70px 0 0;background:linear-gradient(120deg,#2b2f36 0%,#c9ced6 50%,#6ea6dc 100%)"></div>
    <h3>Sterilization Solution</h3>
    <p>Pilvarotek Medical is committed to partner with our customers in finding the most efficient sterilization methodology</p>
  </article>
  <article class="service-card featured" style="left:449px;width:318px">
    <div class="media" role="img" aria-label="Gloved hands sealing a surgical instrument in a pouch" style="border-radius:70px 70px 0 0;background:linear-gradient(120deg,#3f7fd0 0%,#dfe8f2 45%,#f4f6f8 70%,#4a93cf 100%)"></div>
    <h3>Packaging &amp; Cleaning</h3>
    <p>Pilvarotek Medical is committed to partner with our customers in finding the most efficient sterilization methodology</p>
  </article>
  <article class="service-card" style="left:776px;width:302px">
    <div class="media" role="img" aria-label="Automated assembly machine with glass enclosure" style="border-radius:0 70px 0 0;background:linear-gradient(120deg,#1b1f27 0%,#5d6675 45%,#c3cbd6 80%,#7e8896 100%)"></div>
    <h3>Quality Assembly</h3>
    <p>Pilvarotek Medical is committed to partner with our customers in finding the most efficient sterilization methodology</p>
  </article>
  <svg class="abs" style="top:1860px;left:0" width="1200" height="150" viewBox="0 0 1200 150">
    <path d="M0 105 C350 10 800 0 1200 130 L1200 150 L0 150 Z" fill="#ffffff"/>
    <path d="M0 105 C350 10 800 0 1200 130" fill="none" stroke="#0a3553" stroke-width="10"/>
  </svg>
</section>

<section>
  <div class="abs why-copy">
    <h2 class="section-title" style="font-size:36px">Why <strong>Pilvarotek Medical</strong></h2>
    <div class="rule"></div>
    <p class="body" style="margin-top:26px;font-size:15.5px;line-height:26px">Pilvarotek offers deep and vast knowledge in the realm of sterilization and, in particular, detailed guidance with our vertically integrated Hydrogen Peroxide Gas Plasma sterilization modality.</p>
    <p class="body" style="margin-top:20px;font-size:15.5px;line-height:26px">Assistance with the development and comparisons of full validation and batch release can be provided to OEMs &nbsp;to help you select the best path forward</p>
  </div>
  <div class="abs why-frame"></div>
  <div class="abs why-photo" role="img" aria-label="Gloved hand placing a test vial into a laboratory incubator"></div>
</section>

<section>
  <div class="abs features"></div>
  <article class="feature" style="left:115px">
    <div class="feature-icon"><div class="disc">
      <svg width="44" height="44" viewBox="0 0 24 24" fill="none" stroke="#fff" stroke-width="1.6"><path d="M12 22s7-7.5 7-12.5A7 7 0 0 0 5 9.5C5 14.5 12 22 12 22z"/><circle cx="12" cy="9.5" r="2.6"/></svg>
    </div></div>
    <h3>Our <strong>Location</strong></h3>
    <p>Pilvarotek Medical is located on the beautiful Central Coast of California mid-way between San Francisco and Los Angeles.</p>
  </article>
  <article class="feature" style="left:446px;width:311px">
    <div class="feature-icon"><div class="disc dark">
      <svg width="44" height="44" viewBox="0 0 24 24" fill="none" stroke="#fff" stroke-width="1.6"><rect x="4" y="6" width="16" height="15"/><path d="M4 11h16M9 21v-5h6v5M8 3h8v3"/></svg>
    </div></div>
    <h3>Our <strong>Facility</strong></h3>
    <p>Pilvarotek Medical is located on the beautiful Central Coast. Our modern 20,000 square foot facility was designed to exceed today's regulatory requirements and has over 2500 square feet of clean-room and support area designed</p>
  </article>
  <article class="feature" style="left:776px">
    <div class="feature-icon"><div class="disc">
      <svg width="44" height="44" viewBox="0 0 24 24" fill="none" stroke="#fff" stroke-width="1.6"><circle cx="8" cy="8" r="3"/><circle cx="16" cy="8" r="3"/><circle cx="12" cy="15" r="3"/><path d="M4 20c2-2 5-2 8 0s6 2 8 0"/></svg>
    </div></div>
    <h3>Our <strong>Expertise</strong></h3>
    <p>Pilvarotek Medical's areas of expertise include manufacturing and packaging specialties, process and sterility validation studies, environmental controls, and bringing new products to market.</p>
  </article>
</section>

<section>
  <svg class="abs" style="top:3070px;left:108px" width="450" height="450" viewBox="0 0 450 450">
    <path d="M225 7 A218 218 0 1 1 7 225" fill="none" stroke="#1a78b4" stroke-width="7"/>
    <path d="M7 225 A218 218 0 0 1 225 7" fill="none" stroke="#0e3f63" stroke-width="2"/>
  </svg>
  <div class="abs contact-photo" role="img" aria-label="Technician in hair net and gown working at a cleanroom bench"></div>
  <div class="abs contact-copy">
    <h2 class="section-title" style="font-size:36px">Contact <strong>Pilvarotek Medical</strong></h2>
  </div>
  <div class="field" style="top:3168px;height:44px">Name*</div>
  <div class="field" style="top:3223px;height:43px">E-mail address*</div>
  <div class="field" style="top:3274px;height:43px">Phone*</div>
  <div class="field" style="top:3326px;height:92px">Message</div>
  <a class="btn btn-outline" style="top:3435px;left:605px;width:182px;height:54px">Send Message</a>
</section>

<footer>
  <div class="abs site-footer"></div>
  <div class="abs foot-brand"><span class="brand-dot"></span><span class="brand-name">Pilvarotek</span></div>
  <div class="foot-sep" style="left:394px"></div>
  <div class="foot-sep" style="left:626px"></div>
  <div class="foot-sep" style="left:898px"></div>
  <div class="foot-col" style="left:423px">
    <h4>NAVIGATION</h4>
    <ul><li>About Us</li><li>Services</li><li>Pricing</li><li>Contact Us</li></ul>
  </div>
  <div class="foot-col" style="left:656px">
    <h4>CONTACT US</h4>
    <div class="addr">1480 Harbor Ln, Cedar Bay,<br>CA 90021<br>info@pilvarotek.com<br>(555) 201-4410<br>(555) 201-4471</div>
  </div>
  <div class="foot-col" style="left:929px">
    <h4>GET IN TOUCH</h4>
    <div class="social"><span class="mark"></span><div><small>Follow us</small><b>Social Page</b></div></div>
    <div class="social"><span class="mark"></span><div><small>Follow us</small><b>Photo Feed</b></div></div>
  </div>
  <div class="abs foot-line"></div>
  <div class="abs copyright">© Copyright 2021 &nbsp;Pilvarotek Medical</div>
</footer>

</body>
</html>
```